STI/STD Medical Clinic- Wellspring Crest Partners, Inc Website

We are a STI clinic in florida looking for a website. We want to be professional but also playful. We want a buildout similar to the website listed below as our clinic is very similar to theirs.

This is a great example of a clinic doing similar stuff as us. We obviously do not want their color scheme but their format and buildout work. Please see our logo attached for color schemes etc.

https://bluefernclinicmiami.org

Industry/Entity Type

Medical

Coding

Coded - Design and coding required

Number of Pages Required

5+ page

Font styles to use
Sans Serif

```html
<!DOCTYPE html>
<html lang="en">
<head>
<meta charset="utf-8">
<title>Wellspring Crest Partners</title>
<link href="https://fonts.googleapis.com/css2?family=Poppins:wght@300;400;500;600&display=swap" rel="stylesheet">
<style>
:root{
  --blue:#0b8ef3;
  --violet:#5a3be9;
  --purple:#7b3fe8;
  --pink:#e640d2;
  --rose:#ff4fa6;
  --coral:#ff6b45;
  --ink:#2b2b33;
  --muted:#55555e;
  --grey:#f4f4f5;
  --white:#ffffff;
  --grad:linear-gradient(90deg,var(--violet),var(--pink));
}
*{box-sizing:border-box;margin:0;padding:0}
html,body{width:1200px;height:4003px;overflow:hidden}
body{position:relative;font-family:'Poppins',sans-serif;color:var(--ink);background:var(--white)}
.abs{position:absolute}
.backdrop{position:absolute;left:0;top:0;width:1200px;height:4003px;z-index:0}
.layer{position:absolute;z-index:1}

.hero-photo{position:absolute;left:0;top:0;width:1200px;height:672px;background:linear-gradient(180deg,#3a4f68 0%,#2d3d55 45%,#4a4a52 75%,#2a2f38 100%);z-index:1}
.grey-band{position:absolute;left:0;top:672px;width:1200px;height:397px;background:var(--grey);z-index:1}

.topbar{position:absolute;left:567px;top:0;width:633px;height:68px;background:var(--grad);border-bottom-left-radius:40px;z-index:2}
.pill{position:absolute;top:12px;height:39px;background:var(--white);border-radius:20px;font-size:12px;font-weight:600;color:#222;display:flex;align-items:center;justify-content:center}
.brand{position:absolute;display:flex;align-items:center;gap:12px;z-index:2}
.brand-dot{width:44px;height:44px;border-radius:50%;background:var(--purple)}
.brand-name{font-size:30px;font-weight:600;color:var(--white);letter-spacing:1px}
.nav{position:absolute;top:97px;left:0;width:1200px;z-index:2}
.nav a{position:absolute;font-size:15px;color:var(--white);text-decoration:none}
.nav a.current{color:var(--pink)}
.hero-title{position:absolute;top:322px;width:1200px;text-align:center;font-size:48px;font-weight:600;color:var(--white);z-index:2;letter-spacing:.5px}
.btn{position:absolute;display:flex;align-items:center;justify-content:center;border-radius:30px;background:var(--grad);color:var(--white);font-weight:500;z-index:3}
.btn-outline{border:2px solid var(--white)}

.card{position:absolute;width:280px;height:293px;border-radius:6px;z-index:3;color:var(--white);text-align:center}
.card svg{position:absolute;left:110px;top:30px}
.card h3{position:absolute;top:124px;width:100%;font-size:17px;font-weight:500}
.card p{position:absolute;top:158px;left:36px;width:208px;font-size:10.5px;line-height:14px}
.card .more{position:absolute;top:229px;left:78px;width:124px;height:34px;border-radius:18px;background:var(--white);font-size:12px;display:flex;align-items:center;justify-content:center}
.card-blue{background:linear-gradient(160deg,var(--blue),var(--violet))}
.card-violet{background:linear-gradient(160deg,var(--violet),var(--pink))}
.card-rose{background:linear-gradient(160deg,var(--rose),var(--coral))}
.side-tab{position:absolute;left:1145px;top:777px;width:78px;height:78px;border-radius:50%;background:var(--blue);z-index:3}

.section-title{position:absolute;font-size:34px;font-weight:500;color:var(--ink);z-index:2}
.copy{position:absolute;width:445px;font-size:14px;line-height:16.5px;color:var(--muted);z-index:2}
.copy p+p{margin-top:20px}
.photo-circle{position:absolute;border-radius:50%;z-index:2}

.services-title{position:absolute;top:2358px;width:1200px;text-align:center;font-size:32px;font-weight:500;color:var(--white);z-index:2}
.service{position:absolute;top:2458px;width:190px;text-align:center;color:var(--white);z-index:2}
.service .ring{width:126px;height:126px;margin:0 auto;border:2px solid var(--white);border-radius:50%;display:flex;align-items:center;justify-content:center}
.service h4{margin-top:22px;font-size:17px;font-weight:500}
.service p{margin-top:4px;font-size:12px;line-height:15px}

.booking-title{position:absolute;top:2925px;width:1200px;text-align:center;font-size:40px;font-weight:400;line-height:41px;color:var(--white);z-index:2}
.field{position:absolute;background:var(--white);font-size:14px;color:#444;padding-left:18px;display:flex;align-items:center;z-index:2}
.field-area{align-items:flex-start;padding-top:18px}

.foot-head{position:absolute;top:3546px;font-size:17px;font-weight:500;color:#333;z-index:2}
.foot-text{position:absolute;font-size:11.5px;line-height:15px;color:#444;z-index:2}
.foot-links{position:absolute;left:671px;top:3580px;list-style:none;font-size:12px;line-height:22px;color:#444;z-index:2}
.social{position:absolute;top:3669px;width:46px;height:46px;border:2px solid var(--purple);border-radius:50%;z-index:2}
.rule{position:absolute;left:120px;width:979px;height:1px;background:#ddd;z-index:2}
.contact{position:absolute;top:3829px;display:flex;align-items:center;gap:12px;font-size:13.5px;line-height:18px;color:#333;z-index:2}
.contact .icon{width:50px;height:50px;border:2px solid var(--purple);border-radius:50%;display:flex;align-items:center;justify-content:center}
.copyright{position:absolute;top:3955px;width:1200px;text-align:center;font-size:12.5px;color:#333;z-index:2}
</style>
</head>
<body>

<svg class="backdrop" viewBox="0 0 1200 4003" aria-hidden="true">
  <defs>
    <linearGradient id="bookGrad" x1="0" y1="0" x2="1" y2="0">
      <stop offset="0" stop-color="#0b8ef3"/><stop offset="1" stop-color="#5a3be9"/>
    </linearGradient>
    <linearGradient id="servGrad" x1="0" y1="0" x2="1" y2="1">
      <stop offset="0" stop-color="#5a3be9"/><stop offset="0.55" stop-color="#a43fe0"/><stop offset="1" stop-color="#f044c8"/>
    </linearGradient>
    <linearGradient id="arcGrad" x1="0" y1="0" x2="1" y2="0">
      <stop offset="0" stop-color="#5a3be9"/><stop offset="1" stop-color="#e640d2"/>
    </linearGradient>
  </defs>
  <rect x="0" y="2700" width="1200" height="860" fill="url(#bookGrad)"/>
  <path d="M0,2316 Q600,2098 1200,2316 L1200,2782 Q600,2944 0,2782 Z" fill="url(#servGrad)"/>
  <path d="M60,3522 Q600,3345 1140,3522" fill="none" stroke="url(#arcGrad)" stroke-width="7"/>
  <path d="M0,3535 Q600,3360 1200,3535 L1200,4003 L0,4003 Z" fill="#ffffff"/>
</svg>

<div class="hero-photo" role="img" aria-label="Evening city skyline with tall office towers and an elevated bridge"></div>
<div class="grey-band"></div>

<div class="topbar">
  <span class="pill" style="left:25px;width:142px">PATIENT PORTAL</span>
  <span class="pill" style="left:176px;width:221px">PATIENT MESSAGING APP</span>
  <span class="pill" style="left:408px;width:102px">DONATE</span>
</div>

<div class="brand" style="left:121px;top:58px">
  <span class="brand-dot"></span><span class="brand-name">WCP</span>
</div>

<nav class="nav">
  <a class="current" style="left:409px">HOME</a>
  <a style="left:491px">ABOUT</a>
  <a style="left:581px">MEET THE TEAM</a>
  <a style="left:738px">SERVICES</a>
  <a style="left:845px">NEWS</a>
  <a style="left:926px">FAQS</a>
  <a style="left:1002px">CONTACT</a>
</nav>

<h1 class="hero-title">WELLSPRING CREST PARTNERS</h1>
<div class="btn btn-outline" style="left:455px;top:404px;width:289px;height:58px;font-size:16px">BOOK AN APPOINTMENT</div>

<div class="card card-blue" style="left:149px;top:636px">
  <svg width="60" height="76" viewBox="0 0 60 76" fill="none" stroke="#fff" stroke-width="2.5"><rect x="4" y="8" width="52" height="64" rx="4"/><rect x="18" y="3" width="24" height="10" rx="2"/><path d="M30 22v16M22 30h16M12 48h6M24 48h24M12 58h6M24 58h24"/></svg>
  <h3>PREP</h3>
  <p>Lorem ipsum dolor sit amet, consect adipiscing elit, sed do eiusmod tempor incididunt ut labore et dolorena</p>
  <span class="more" style="color:var(--violet)">READ MORE</span>
</div>
<div class="card card-violet" style="left:458px;top:598px">
  <svg width="68" height="68" viewBox="0 0 68 68" fill="none" stroke="#fff" stroke-width="2.5"><rect x="4" y="14" width="60" height="50" rx="8"/><path d="M24 14V6h20v8"/><path d="M28 26h12v8h8v12h-8v8H28v-8h-8V34h8z"/></svg>
  <h3>HEPATITIS C</h3>
  <p>Lorem ipsum dolor sit amet, consect adipiscing elit, sed do eiusmod tempor incididunt ut labore et dolorena</p>
  <span class="more" style="color:var(--pink)">READ MORE</span>
</div>
<div class="card card-rose" style="left:766px;top:636px">
  <svg width="60" height="76" viewBox="0 0 60 76" fill="none" stroke="#fff" stroke-width="2.5"><path d="M30 40C20 26 18 18 22 10c4-7 12-7 16 0 4 8 2 16-8 30L14 70M30 40l16 30"/></svg>
  <h3>HIV</h3>
  <p>Lorem ipsum dolor sit amet, consect adipiscing elit, sed do eiusmod tempor incididunt ut labore et dolorena</p>
  <span class="more" style="color:var(--coral)">READ MORE</span>
</div>
<div class="side-tab"></div>

<h2 class="section-title" style="left:154px;top:1186px">ABOUT OUR CLINIC</h2>
<div class="copy" style="left:154px;top:1258px">
  <p>Lorem ipsum dolor sit amet, consectetur adipiscing elit, sed do eiusmod tempor incididunt ut labore et dolore magna aliquaus ipsum suspendisse ultrices gravida. Risus commodo viverra amaecenas accumsan lacus vel facilisis.</p>
  <p>Lorem ipsum dolor sit amet, consectetur adipiscing elit, sed do eiusmod tempor incididunt ut labore et dolore magna aliquaus ipsum suspendisse ultrices gravida. Risus commodo viverra amaecenas accumsan lacus vel facilisis.</p>
</div>
<div class="btn" style="left:154px;top:1436px;width:175px;height:59px;font-size:17px">ABOUT US</div>
<div class="photo-circle" style="left:656px;top:1189px;width:404px;height:404px;background:radial-gradient(circle at 40% 40%,#f3e6e0,#c9cbd6 60%,#8ea2b8)" role="img" aria-label="Doctor in a white coat speaking with a patient seated on an exam chair"></div>

<div class="photo-circle" style="left:108px;top:1660px;width:120px;height:120px;background:linear-gradient(160deg,var(--violet),var(--pink));z-index:1"></div>
<div class="photo-circle" style="left:115px;top:1644px;width:466px;height:466px;background:radial-gradient(circle at 50% 45%,#eef2f6,#c8dbe8 60%,#9bbfd8)" role="img" aria-label="Smiling group of doctors and nurses in white coats and blue scrubs"></div>
<h2 class="section-title" style="left:629px;top:1734px">MEET OUR TEAM</h2>
<div class="copy" style="left:629px;top:1806px">
  <p>Lorem ipsum dolor sit amet, consectetur adipiscing elit, sed do eiusmod tempor incididunt ut labore et dolore magna aliquaus ipsum suspendisse ultrices gravida. Risus commodo viverra amaecenas accumsan lacus vel facilisis.</p>
  <p>Lorem ipsum dolor sit amet, consectetur adipiscing elit, sed do eiusmod tempor incididunt ut labore et dolore magna aliquaus ipsum suspendisse ultrices gravida. Risus commodo viverra amaecenas accumsan lacus vel facilisis.</p>
</div>
<div class="btn" style="left:629px;top:1984px;width:176px;height:59px;font-size:17px">MEET NOW</div>

<h2 class="services-title">OUR SERVICES</h2>
<div class="service" style="left:81px">
  <div class="ring"><svg width="50" height="62" viewBox="0 0 60 76" fill="none" stroke="#fff" stroke-width="2.5"><rect x="4" y="8" width="52" height="64" rx="4"/><rect x="18" y="3" width="24" height="10" rx="2"/><path d="M30 22v16M22 30h16M12 48h6M24 48h24M12 58h6M24 58h24"/></svg></div>
  <h4>PREP</h4><p>STaLorem ipsum dolor sit a met, consectetur adipiscina od gravida. Risus odo</p>
</div>
<div class="service" style="left:287px">
  <div class="ring"><svg width="56" height="60" viewBox="0 0 56 60" fill="none" stroke="#fff" stroke-width="2.5"><path d="M8 4v18a12 12 0 0 0 24 0V4M20 34v10a10 10 0 0 0 20 0V30"/><circle cx="40" cy="22" r="7"/></svg></div>
  <h4>PEP</h4><p>Lorem ipsum dolor sit a met, consectetur adipiscina od gravida. Risus odo</p>
</div>
<div class="service" style="left:494px">
  <div class="ring"><svg width="58" height="58" viewBox="0 0 68 68" fill="none" stroke="#fff" stroke-width="2.5"><rect x="4" y="14" width="60" height="50" rx="8"/><path d="M24 14V6h20v8"/><path d="M28 26h12v8h8v12h-8v8H28v-8h-8V34h8z"/></svg></div>
  <h4>HEPATITIS C</h4><p>STaLorem ipsum dolor sit a met, consectetur adipiscina od gravida. Risus odo</p>
</div>
<div class="service" style="left:701px">
  <div class="ring"><svg width="54" height="60" viewBox="0 0 54 60" fill="none" stroke="#fff" stroke-width="2.5"><circle cx="27" cy="18" r="12"/><path d="M4 58v-8c0-10 10-16 23-16s23 6 23 16v8z"/></svg></div>
  <h4>STI</h4><p>STaLorem ipsum dolor sit a met, consectetur adipiscina od gravida. Risus odo</p>
</div>
<div class="service" style="left:907px">
  <div class="ring"><svg width="60" height="60" viewBox="0 0 60 60" fill="none" stroke="#fff" stroke-width="2.5"><path d="M8 10l10-4 8 14-6 5c3 7 8 12 15 15l5-6 14 8-4 10C30 52 8 30 8 10z"/><circle cx="44" cy="16" r="10"/><path d="M44 11v10M39 16h10"/></svg></div>
  <h4>TELEHEALTH</h4><p>STaLorem ipsum dolor sit a met, consectetur adipiscina od gravida. Risus odo</p>
</div>
<div class="btn" style="left:513px;top:2741px;width:174px;height:58px;font-size:17px;background:linear-gradient(90deg,var(--blue),var(--violet))">VIEW MORE</div>

<h2 class="booking-title">Now Booking For TeleHealth<br>&amp; In-Person Appointments</h2>
<div class="field" style="left:258px;top:3054px;width:344px;height:53px">Name</div>
<div class="field" style="left:615px;top:3054px;width:343px;height:53px">Email</div>
<div class="field" style="left:258px;top:3122px;width:344px;height:53px">Phone</div>
<div class="field" style="left:615px;top:3122px;width:343px;height:53px">Subject</div>
<div class="field field-area" style="left:258px;top:3192px;width:698px;height:132px">Message</div>
<div class="btn" style="left:535px;top:3301px;width:146px;height:51px;font-size:16px">SUBMIT</div>

<div class="brand" style="left:121px;top:3584px">
  <span class="brand-dot"></span><span class="brand-name" style="color:var(--purple)">WCP</span>
</div>
<span class="social" style="left:154px"></span>
<span class="social" style="left:210px"></span>
<span class="social" style="left:268px"></span>

<h3 class="foot-head" style="left:396px">ABOUT</h3>
<p class="foot-text" style="left:396px;top:3582px;width:230px">Lorem ipsum dolor sit am tconsec tetur adipiscig elit sed do eiusmod tem por incididunt ut lablorore et dolore Lorem ipsum dolorsit am etconsectetur adipiscig elit sed do eiusmod teincididunt .</p>

<h3 class="foot-head" style="left:671px">LINKS</h3>
<ul class="foot-links">
  <li>Home</li><li>About</li><li>Services</li><li>FAQ</li><li>Resources</li><li>Employment</li><li>Contact</li>
</ul>

<h3 class="foot-head" style="left:817px">NEWSLETTER</h3>
<p class="foot-text" style="left:817px;top:3583px;width:245px">Lorem ipsum dolor sit am etcons ectetur adipiscig elit sed do eiusmod tem por incididunt ut lablorore</p>
<div class="field" style="left:817px;top:3646px;width:241px;height:40px;background:#f3f3f5;border-radius:20px;font-size:12px">Email:</div>
<div class="btn" style="left:817px;top:3702px;width:241px;height:40px;font-size:15px">SUBMIT</div>

<div class="rule" style="top:3783px"></div>
<div class="contact" style="left:272px">
  <span class="icon"><svg width="22" height="22" viewBox="0 0 24 24" fill="var(--purple)"><path d="M5 3l4-1 2 6-3 2c1 3 3 5 6 6l2-3 6 2-1 4C11 20 4 13 5 3z"/></svg></span>
  <span>Call us:<br>555 014 2387</span>
</div>
<div class="contact" style="left:486px">
  <span class="icon"><svg width="20" height="24" viewBox="0 0 20 24" fill="var(--purple)"><path d="M10 1a8 8 0 0 0-8 8c0 6 8 14 8 14s8-8 8-14a8 8 0 0 0-8-8zm0 11a3 3 0 1 1 0-6 3 3 0 0 1 0 6z"/></svg></span>
  <span>Address:<br>Location name lore56</span>
</div>
<div class="contact" style="left:736px">
  <span class="icon"><svg width="22" height="16" viewBox="0 0 22 16" fill="var(--purple)"><path d="M0 0h22v16H0zM2 2l9 7 9-7" stroke="#fff" stroke-width="1.5"/></svg></span>
  <span>Email:<br>hello@wellspringcrest.org</span>
</div>
<div class="rule" style="top:3935px"></div>
<p class="copyright">Copyrights © 2022 All Rights Reversed</p>

</body>
</html>
```